Conference banner for Kestrel training organisation

We empower everyday heroes.
We provide training that empowers individuals to create positive change in themselves, their community, and the world.
We need a large banner design to promote the organisation at conferences and events. We are open to ideas and creativity.
It may involve creatively displaying our logo only, or it may involve our logo and a summary of our products (Kestrel training, Calm Minds Field Care).
Size: 820mm width x 1790mm height
300dpi
Target Market(s)
Educators and frontline health, community, and social workers.
Industry/Entity Type
Training
Colors
Designer to choose colors to be used in the design.

```html
<!DOCTYPE html>
<html lang="en">
<head>
<meta charset="utf-8">
<title>Kestrel Commons – Conference Banner</title>
<link href="https://fonts.googleapis.com/css2?family=Lato:ital,wght@0,300;0,400;0,700;0,900;1,400&display=swap" rel="stylesheet">
<style>
  :root {
    --stage: #e9eaec;
    --sheet: #ffffff;
    --sheet-shade: #f1f2f4;
    --brand-blue: #2f68b2;
    --brand-blue-light: #4a80c6;
    --brand-maroon: #b2304c;
    --caption-band: rgba(110, 30, 40, 0.82);
    --body-grey: #7b7f86;
    --photo-sky: #c9d2d8;
    --photo-green: #3f5a3a;
    --photo-earth: #5a2e2c;
  }
  * { box-sizing: border-box; margin: 0; padding: 0; }
  html, body {
    width: 1200px; height: 823px; overflow: hidden;
    background: var(--stage);
    font-family: "Lato", Arial, sans-serif;
  }
  .banner {
    position: absolute; left: 400px; top: 11px;
    width: 400px; height: 800px;
    background: linear-gradient(180deg, var(--sheet) 0%, var(--sheet-shade) 100%);
    box-shadow: 0 4px 18px rgba(0,0,0,0.12);
  }
  .brand-name {
    position: absolute; right: 24px; top: 50px;
    font-weight: 700; font-size: 11px; letter-spacing: 0.4px;
    color: var(--brand-blue); text-transform: uppercase;
  }
  .brand-dot {
    position: absolute; right: 52px; top: 26px;
    width: 18px; height: 18px; border-radius: 50%;
    background: var(--brand-blue);
  }
  .headline-band {
    position: absolute; left: 16px; top: 92px;
    width: 376px; height: 78px;
    background: linear-gradient(90deg, var(--brand-blue) 0%, var(--brand-blue-light) 100%);
    padding: 14px 26px;
    color: #fff; font-weight: 700; font-size: 21px; line-height: 26px;
  }
  .mission {
    position: absolute; left: 42px; top: 192px; width: 330px;
    color: var(--brand-maroon); font-size: 15.5px; line-height: 19px; font-weight: 400;
  }
  .offer { position: absolute; left: 36px; width: 330px; }
  .offer-icon { position: absolute; left: 0; top: 8px; width: 32px; height: 32px; }
  .offer-title {
    margin-left: 56px; color: var(--brand-blue);
    font-size: 11.5px; font-weight: 700; margin-bottom: 6px;
  }
  .offer-text {
    margin-left: 56px; color: var(--body-grey);
    font-size: 8.6px; line-height: 11px; font-weight: 400; width: 220px;
  }
  .offer-training { top: 276px; }
  .offer-mindful { top: 334px; }
  .offer-fieldcare { top: 402px; }
  .hero-photo {
    position: absolute; left: 16px; top: 484px;
    width: 376px; height: 258px;
    background: linear-gradient(180deg, var(--photo-sky) 0%, #b9c4c6 45%, var(--photo-green) 80%, var(--photo-earth) 100%);
    overflow: hidden;
  }
  .hero-caption {
    position: absolute; left: 0; bottom: 0; width: 100%; height: 36px;
    background: var(--caption-band);
    color: #fff; font-style: italic; font-size: 14px;
    display: flex; align-items: center; justify-content: center;
  }
  .site-address {
    position: absolute; left: 0; top: 766px; width: 100%; text-align: center;
    color: var(--brand-blue); font-weight: 900; font-size: 14px; letter-spacing: 1.6px;
  }
</style>
</head>
<body>
  <main class="banner">
    <span class="brand-dot"></span>
    <div class="brand-name">Kestrel Commons</div>

    <div class="headline-band">Re-write your story<br>&amp; Become a hero</div>

    <p class="mission">Kestrel Commons is dedicated to educate, inspire, and support individuals in the path to fulfill their potential.</p>

    <section class="offer offer-training">
      <svg class="offer-icon" viewBox="0 0 32 32" aria-hidden="true">
        <circle cx="16" cy="16" r="16" fill="var(--brand-blue)"/>
        <circle cx="16" cy="9.5" r="3" fill="#fff"/>
        <path d="M16 13 L21.5 24 H10.5 Z" fill="#fff"/>
      </svg>
      <h3 class="offer-title">Everyday Kestrel Training</h3>
      <p class="offer-text">Gain practical tools and resources to foster change in yourself, your community, and the world.</p>
    </section>

    <section class="offer offer-mindful">
      <svg class="offer-icon" viewBox="0 0 32 32" aria-hidden="true">
        <circle cx="16" cy="16" r="16" fill="var(--brand-blue)"/>
        <circle cx="14.5" cy="14.5" r="6" fill="none" stroke="#fff" stroke-width="2.4"/>
        <line x1="19" y1="19" x2="24" y2="24" stroke="#fff" stroke-width="2.8" stroke-linecap="round"/>
      </svg>
      <h3 class="offer-title">Mindfulness Classes</h3>
      <p class="offer-text">Explore a variety of mindfulness techniques on the journey toward finding what works for you.</p>
    </section>

    <section class="offer offer-fieldcare">
      <svg class="offer-icon" viewBox="0 0 32 32" aria-hidden="true">
        <circle cx="16" cy="16" r="16" fill="var(--brand-blue)"/>
        <rect x="13" y="7" width="6" height="18" fill="#fff"/>
        <rect x="7" y="13" width="18" height="6" fill="#fff"/>
      </svg>
      <h3 class="offer-title">Calm Minds Field Care</h3>
      <p class="offer-text">Gain the ability to recognise and respond to mentalhealth crises, including suicidal thoughts, deliberate self-harm, and more.</p>
    </section>

    <div class="hero-photo" role="img" aria-label="Photo of a child in a pink cape leaping through the air between pine trees by a lake">
      <div class="hero-caption">Overcome challenges!</div>
    </div>

    <div class="site-address">WWW.KESTRELCOMMONS.COM.AU</div>
  </main>
</body>
</html>
```